Start up in business consultancy needs a business card

We need the business card's layout (we have already the logo). Our business is concerned on consultancy services delivered to companies on the matter of sustainability. Business card should be enough essentials and professional style.

Side A with the following info:
logo + a space for the claim (still to identify) + website of the company

Side B with the following info:
Name of business card holder + title of the business card holder + address of the company + space for mobile number, phone number, fax number + e-mail of business card holder + graphic details around.

Target Market(s)

Business of any sector

Industry/Entity Type

Business Service

Contact Information for Business Card

Name of the company:
Pianoverde srl
Società Benefit

Address of the company:
Via Lucerna, 7
21047 - Saronno (VA)

Website:
www.pianoverde.it

Name of the BC' holder:
Luca Ferentino

Title:
Co-fondatore

Email:
luca@pianoverde.it

Mobile:
+39 348 915 2074
Phone:
+39 348 915 2074
Fax:
+39 348 915 2074

Font styles to use
Other font styles liked:
• new gothic

```html
<!DOCTYPE html>
<html lang="it">
<head>
<meta charset="utf-8">
<title>Pianoverde srl – Biglietto da visita</title>
<link rel="stylesheet" href="https://fonts.googleapis.com/css2?family=Lato:ital,wght@0,400;0,700;0,900;1,400&display=swap">
<style>
  :root {
    --brand-blue: #0f67ae;
    --brand-blue-soft: rgba(255, 255, 255, 0.14);
    --card-white: #ffffff;
    --icon-blue: #1d8fd6;
    --stage: #e9ecef;
  }
  * { box-sizing: border-box; margin: 0; padding: 0; }
  html, body {
    width: 1200px; height: 900px; overflow: hidden;
    background: var(--stage);
    font-family: "Lato", sans-serif;
  }
  .sheet {
    position: relative; width: 1200px; height: 900px;
    display: flex; flex-direction: column; align-items: center; justify-content: center; gap: 36px;
  }
  .card {
    position: relative; width: 660px; height: 390px; overflow: hidden;
    box-shadow: 0 6px 22px rgba(0, 0, 0, 0.18);
  }

  /* Side A */
  .card--front { background: var(--brand-blue); color: var(--card-white); }
  .front__ring {
    position: absolute; right: -130px; top: 60px;
    width: 400px; height: 400px; border-radius: 50%;
    border: 16px solid var(--brand-blue-soft);
  }
  .front__brand {
    position: absolute; left: 190px; top: 132px;
    display: flex; align-items: center; gap: 18px;
  }
  .brand-dot {
    width: 74px; height: 74px; border-radius: 50%;
    border: 5px solid currentColor; flex: none;
  }
  .brand-name { font-weight: 700; font-size: 44px; letter-spacing: 0.5px; line-height: 1; }
  .front__web {
    position: absolute; left: 282px; top: 196px;
    font-size: 16px; letter-spacing: 0.6px;
  }

  /* Side B */
  .card--back { background: var(--card-white); color: var(--brand-blue); }
  .back__brand {
    position: absolute; left: 250px; top: 42px;
    display: flex; align-items: center; gap: 20px;
  }
  .back__brand .brand-dot { width: 96px; height: 96px; border-width: 6px; }
  .back__brand .brand-name { font-size: 50px; }
  .back__rule {
    position: absolute; left: 0; right: 0; top: 186px;
    height: 2px; background: var(--brand-blue);
  }
  .holder { position: absolute; left: 40px; top: 136px; }
  .holder__name { font-weight: 900; font-size: 21px; text-transform: uppercase; letter-spacing: 0.2px; }
  .holder__title { font-style: italic; font-size: 15px; color: var(--icon-blue); margin-top: 1px; }

  .address-tab {
    position: absolute; left: 0; bottom: 0; width: 330px; height: 78px;
  }
  .address-tab svg { position: absolute; inset: 0; }
  .address-tab__text {
    position: absolute; left: 34px; top: 24px;
    color: var(--card-white); font-size: 17px; letter-spacing: 0.3px;
  }

  .contacts {
    position: absolute; left: 390px; top: 214px; list-style: none;
    font-size: 18px; line-height: 1.42;
  }
  .contacts li { display: flex; align-items: center; gap: 12px; }
  .contacts svg { width: 18px; height: 18px; flex: none; fill: none; stroke: var(--icon-blue); stroke-width: 1.8; }
</style>
</head>
<body>
<main class="sheet">

  <section class="card card--front" aria-label="Fronte del biglietto">
    <div class="front__ring" aria-hidden="true"></div>
    <div class="front__brand">
      <span class="brand-dot" aria-hidden="true"></span>
      <span class="brand-name">pianoverde</span>
    </div>
    <p class="front__web">www.pianoverde.it</p>
  </section>

  <section class="card card--back" aria-label="Retro del biglietto">
    <div class="back__brand">
      <span class="brand-dot" aria-hidden="true"></span>
      <span class="brand-name">pianoverde</span>
    </div>
    <div class="back__rule" aria-hidden="true"></div>

    <div class="holder">
      <p class="holder__name">Luca Ferentino</p>
      <p class="holder__title">Co-fondatore</p>
    </div>

    <div class="address-tab">
      <svg viewBox="0 0 330 78" width="330" height="78" aria-hidden="true">
        <path d="M0 78 L0 0 L296 0 Q306 0 309 10 L330 78 Z" fill="var(--brand-blue)"/>
      </svg>
      <p class="address-tab__text">Via Lucerna, 7, 21047 - Saronno (VA)</p>
    </div>

    <ul class="contacts">
      <li>
        <svg viewBox="0 0 18 18" aria-hidden="true"><rect x="5" y="1.5" width="8" height="15" rx="1.5"/><line x1="8" y1="14" x2="10" y2="14"/></svg>
        +39 348 915 2074
      </li>
      <li>
        <svg viewBox="0 0 18 18" aria-hidden="true"><path d="M4 2 L7 2 L8 6 L6 7.5 Q7.5 10.5 10.5 12 L12 10 L16 11 L16 14 Q16 16 14 16 Q3 15 2 4 Q2 2 4 2 Z"/></svg>
        +39 348 915 2074
      </li>
      <li>
        <svg viewBox="0 0 18 18" aria-hidden="true"><rect x="2" y="7" width="14" height="8" rx="1"/><rect x="5" y="2.5" width="8" height="4.5"/><line x1="5" y1="11" x2="13" y2="11"/></svg>
        +39 348 915 2074
      </li>
      <li>
        <svg viewBox="0 0 18 18" aria-hidden="true"><rect x="1.5" y="4" width="15" height="10" rx="1"/><path d="M1.5 4.5 L9 10 L16.5 4.5"/></svg>
        luca@pianoverde.it
      </li>
    </ul>
  </section>

</main>
</body>
</html>
```